Business Card Design for drone videography and photography

I have a Vexor Talon 3 drone. I am looking for a logo to somehow incorporate with my business name. I don't even know what is an appropriate font. I am most filming real estate homes. I want something simplistic and a logo that makes sense for the business that I'm in. xxxxxxxxxxxxxxxxxxxxxxxxxxxxxxxxxxxxxxxxxxxxxxxxxxxxxxxxxxxxxxxxxxxxxxxxxxxxxxxxxxxxxxxxxxxxxxxxxxxxxxxxxxxxxxxxxxxxxxxxxxxxxxxxxxxxxxxxxxxxxxxxxxxxxxxxxxxxxxxxxxxxxxxxxxxxxxxxxxxxxxxxxxxxxxxxxxxxxxxxxxxxxxxxxxxxxxxxxxxxxxxxxxxxxxxxxxxxxxxxxxxxxxxxxxxxxxxxxxxxxxxxxxxxxxxxxxxxxxxxxxxxxxxxxxxxxxxxxxxxxxxxxxxxxxxxxxxxxxxxxxxxxxxxxxxxxxxxxxxxxxxxxxxxxxxxxxxxxxxxxxxxxxxxxxxxxxxxxxxxxxxxxxxxxxxxxxxxxxxxxxxxxxxxxxxxxxxxxxxxxxxxxxxxxxxxxxxxxxxxxxxxxxxxxxxxxxxxxxxxxxxxxxxxxxxxxxxxxxxxxxxxxxxxxxxxxxxxxxxxxxxxxxxxxxxxxxxxxxxxxxxxxxxxxxxxxxxxxxxxxxxxxxxxxxxxxxxxxxxxxxxxxxxxxxxxxxxxxxxxxxxxxxxxxxxxxxxxxxxxxxxxxxxxxxxxxxxxxxxxxxxxxxxxxxxxxxxxxxxxxxxxxxxxxxxxxxxxxxxxxxxxxxxxxxxxxxxxxxxxxxxxxxxxxxxxxxxxxxxxxxxxxxxxxxxxxxxxxxxxxxxxxxxxxxxxxxxxxxxxxxxxxxxxxxxxxxxxxxxxxxxxxxxxxxxxxxxxxxxxxxxxxxxxxxxxxxxxxxxxxxxxxxxxxxxxxxxxxxxxxxxxxxxxxxxxxxxxxxxxxxxxxxxxxxxxxxxxxxxxxxxxxxxxxxxxxxxxxxxxxxxxxxxxxxxxxxxxxxxxxxxxxxxxxxxxxxxxxxxxxxxxxxxxxxxxxxxxxxxxxxxxxxxxxxxxxxxxxxxxxxxxxxxxxxxxxxxxxxxxxxxxxxxxxxxxxxxxxxxxxxxxxxxxxxxxxxxxxxxxxxxxxxxxxxxxxxxxxxxx

Target Market(s)

Real estate

Industry/Entity Type

Business

Contact Information for Business Card

BRANDT SKYVIEW STUDIO
Daniel Brandt
Owner/Operator

48305 Birch Way
Ste. Genevieve MO 63670

314-720-4163
dbrandt@brandtskyviewstudio.example

NCQ Drone Certified
Insured
Section 333 Exempt
Halvo Wing Class Certified

Font styles to use
Other font styles liked:
• PUMP DEMI BOLD LET

Requirements
Must have
• Maybe have the certifications on the back??? The business card must be more serious than playful
Nice to have
• Possibly have the logo work itself into the business name?
Should not have
• nothing that looks like a "fun" business. I want this business card to look professional but also simplistic. I don't want a picture that I took from my drone as the background.

```html
<!DOCTYPE html>
<html lang="en">
<head>
<meta charset="utf-8">
<title>Brandt Skyview Studio – Business Card</title>
<link rel="stylesheet" href="https://fonts.googleapis.com/css2?family=Barlow:wght@400&display=swap">
<style>
  :root {
    --card-bg: #1b1b1b;
    --ink: #f2f2f2;
  }
  html, body {
    margin: 0;
    padding: 0;
    width: 1200px;
    height: 702px;
    overflow: hidden;
    background: var(--card-bg);
  }
  .card {
    position: relative;
    width: 1200px;
    height: 702px;
    background: var(--card-bg);
    color: var(--ink);
    font-family: "Barlow", "Helvetica Neue", Arial, sans-serif;
    font-weight: 400;
    text-transform: uppercase;
  }
  .address {
    position: absolute;
    left: 66px;
    top: 64px;
    font-size: 18px;
    line-height: 23px;
    letter-spacing: 0.02em;
  }
  .identity {
    position: absolute;
    left: 0;
    right: 0;
    top: 326px;
    text-align: center;
  }
  .business-name {
    margin: 0;
    font-size: 55px;
    line-height: 56px;
    font-weight: 400;
    letter-spacing: 0.035em;
  }
  .owner-name {
    margin: 11px 0 0;
    font-size: 29px;
    line-height: 30px;
    letter-spacing: 0.04em;
  }
  .owner-role {
    margin: 8px 0 0;
    font-size: 16px;
    line-height: 17px;
    letter-spacing: 0.04em;
  }
  .credentials {
    position: absolute;
    left: 66px;
    top: 546px;
    margin: 0;
    padding: 0;
    list-style: none;
    font-size: 18px;
    line-height: 22.6px;
    letter-spacing: 0.03em;
  }
  .contact {
    position: absolute;
    right: 72px;
    top: 581px;
    text-align: right;
  }
  .contact-phone {
    display: block;
    font-size: 29px;
    line-height: 30px;
    letter-spacing: 0.04em;
  }
  .contact-email {
    display: block;
    margin-top: 4px;
    font-size: 19px;
    line-height: 20px;
    letter-spacing: 0.04em;
  }
</style>
</head>
<body>
  <main class="card">
    <address class="address" style="font-style: normal;">
      <div>48305 Birch Way</div>
      <div>Ste. Genevieve MO 63670</div>
    </address>

    <section class="identity">
      <h1 class="business-name">Brandt Skyview Studio</h1>
      <p class="owner-name">Daniel Brandt</p>
      <p class="owner-role">Owner/Operator</p>
    </section>

    <ul class="credentials">
      <li>NCQ Drone Certified</li>
      <li>Insured</li>
      <li>Section 333 Exempt</li>
      <li>Halvo Wing Class Certified</li>
    </ul>

    <div class="contact">
      <span class="contact-phone">314-720-4163</span>
      <span class="contact-email">dbrandt@brandtskyviewstudio.example</span>
    </div>
  </main>
</body>
</html>
```